Web App Dashboard Design for Healthcare Company

We have developed a simple web application with 3 navigation menus. We like the current design (very much modeled after Tallyworks), but we want to explore UI options for the branding, header, menus, and footer that we may not have considered.

The attached screenshots show the layout and two menu "hover" views as they currently exist.

This web application is used by employees only.

Menu 1 - Module Menu:
Allows the user to switch easily between Account, Employee, and Care Management.

Menu 2 - Reports Menu
Allows user to view available reports within each Module.

Menu 3 - Admin Menu
Allows the user to easily create new content types within each module.

Use our branded colors and font.

Colors:
Logo Blue (dark): 00c0f3
Logo Blue (light): 44c8f5
Nav Blue: 0994d0
Green: 71b44b
Grayscale: (not specified)

Font:
Lato (Google Font)

Target Market(s)

Internal staff.

Industry/Entity Type

Healthcare

Number of Pages Required

3 page

Font styles to use
Sans Serif
Other font styles liked:
• Lato (Google Font)

Colors
0293ce
9bcb3c

Requirements
Must have
• It's really a one page design, but we want to see the two "hover" views for the Module Menu and the Admin Menu.
• It should also be very clear which "Report" page the user is on (the active menu link).
• Must use branded colors, font, and logo.
• Logo Blue (dark): 00c0f3
• Logo Blue (light): 44c8f5
• Nav Blue: 0994d0
• Green: 71b44b
• Grayscale: Designer may choose
Nice to have
• It would be nice to have simple uncluttered payouts.
Should not have
• The design should not have menu options exposed by default.

```html
<!DOCTYPE html>
<html lang="en">
<head>
<meta charset="utf-8">
<title>CareLedger – Accounts Management</title>
<link href="https://fonts.googleapis.com/css2?family=Lato:wght@400;700&display=swap" rel="stylesheet">
<style>
:root{
  --logo-blue:#00c0f3;
  --sky:#6ec6ef;
  --nav-top:#6cc2ee;
  --nav-bottom:#4aa9dd;
  --green:#71b44b;
  --green-text:#62ad3e;
  --text:#444;
  --muted:#777;
  --line:#dcdcdc;
  --stripe:#f4f4f4;
  --footer:#eeeeee;
}
*{box-sizing:border-box;margin:0;padding:0}
html,body{width:1200px;height:770px;overflow:hidden}
body{position:relative;background:#fff;font-family:'Lato',sans-serif;color:var(--text)}
.header{position:absolute;left:0;top:0;width:1200px;height:77px}
.brand{position:absolute;left:99px;top:22px;display:flex;align-items:center;gap:8px}
.brand-mark{width:22px;height:22px;background:var(--logo-blue);border-radius:50%}
.brand-name{font-size:24px;font-weight:700;color:#2a2a2a}
.module-select{position:absolute;left:243px;top:22px;width:304px;height:34px;border:1px solid #c9c9c9;font-size:11.5px;color:#555;padding:0 13px;display:flex;align-items:center;justify-content:space-between}
.add-btn{position:absolute;left:889px;top:23px;width:32px;height:32px;border-radius:50%;background:var(--green);display:flex;align-items:center;justify-content:center}
.user-link{position:absolute;top:31px;font-size:13px;color:#666;display:flex;align-items:center;gap:6px}
.user-link.info{left:945px}
.user-link.logout{left:1038px}
.navbar{position:absolute;left:0;top:77px;width:1200px;height:40px;background:linear-gradient(var(--nav-top),var(--nav-bottom))}
.nav-item{position:absolute;top:0;height:40px;line-height:40px;font-size:11.5px;font-weight:700;color:#fff;text-transform:uppercase}
.nav-item.active{left:99px;width:152px;text-align:center;background:var(--green)}
.dropdown{position:absolute;list-style:none}
.dropdown li{position:relative;padding-left:28px;font-size:13px}
.dropdown li::before{content:"›";position:absolute;left:14px}
.module-menu{left:363px;top:62px;width:184px;height:76px;background:#fff;border:1px solid #ddd;box-shadow:0 2px 5px rgba(0,0,0,.12);padding-top:14px;color:#666}
.module-menu li{height:27px}
.admin-menu{left:825px;top:69px;width:162px;height:149px;background:var(--green);color:#fff;padding-top:12px}
.admin-menu li{height:25px;font-size:13px}
.admin-menu::before{content:"";position:absolute;left:73px;top:-7px;border:7px solid transparent;border-top:0;border-bottom-color:var(--green)}
.data-table{position:absolute;left:99px;top:147px;width:1002px;border-collapse:collapse;table-layout:fixed;font-size:13px}
.data-table th{height:41px;background:var(--sky);color:#fff;font-size:11.5px;font-weight:700;text-align:left;padding-left:20px;text-transform:uppercase;border-right:1px solid rgba(255,255,255,.3)}
.data-table td{height:41px;padding-left:20px;border:1px solid var(--line);white-space:nowrap}
.data-table tr:nth-child(even) td{background:var(--stripe)}
.data-table td.name{color:var(--green-text)}
.data-table td.last{position:relative}
.row-btn{position:absolute;right:12px;top:11px;width:66px;height:20px;background:var(--green);color:#fff;font-size:8px;line-height:20px;text-align:center;border-radius:2px;text-transform:uppercase}
.footer{position:absolute;left:0;top:724px;width:1200px;height:46px;background:var(--footer);border-top:1px solid #ddd}
.copyright{position:absolute;left:99px;top:16px;font-size:12px;color:#666}
.contact-btn{position:absolute;left:1011px;top:10px;width:89px;height:26px;background:var(--sky);color:#fff;font-size:10px;line-height:26px;text-align:center;text-transform:uppercase;border-radius:2px}
</style>
</head>
<body>
<header class="header">
  <div class="brand"><span class="brand-mark"></span><span class="brand-name">CareLedger</span></div>
  <div class="module-select">Accounts Management
    <svg width="10" height="6" viewBox="0 0 10 6"><path d="M1 1l4 4 4-4" fill="none" stroke="#666" stroke-width="1.3"/></svg>
  </div>
  <div class="add-btn"><svg width="14" height="14" viewBox="0 0 14 14"><path d="M7 0v14M0 7h14" stroke="#fff" stroke-width="1.4"/></svg></div>
  <div class="user-link info"><svg width="15" height="15" viewBox="0 0 15 15" fill="none" stroke="#5bb7e6" stroke-width="1.2"><circle cx="7.5" cy="4.5" r="3.5"/><path d="M1 14.5c0-3.5 3-5.5 6.5-5.5s6.5 2 6.5 5.5z"/></svg>My Info</div>
  <div class="user-link logout"><svg width="15" height="15" viewBox="0 0 15 15" fill="none" stroke="#5bb7e6" stroke-width="1.2"><path d="M8 1H1v13h7M5 7.5h9M11 4.5l3 3-3 3"/></svg>Logout</div>
</header>

<nav class="navbar">
  <span class="nav-item active">Reminders</span>
  <span class="nav-item" style="left:296px">Accounts</span>
  <span class="nav-item" style="left:478px">Contacts</span>
  <span class="nav-item" style="left:638px">Reports</span>
  <span class="nav-item" style="left:775px">My Company</span>
</nav>

<ul class="dropdown module-menu">
  <li>Employee Management</li>
  <li>Care Management</li>
</ul>

<table class="data-table">
  <colgroup><col style="width:207px"><col style="width:172px"><col style="width:163px"><col style="width:155px"><col style="width:305px"></colgroup>
  <thead><tr><th>Es simplemente el</th><th>Las industrias</th><th>Simplemente</th><th>De relleno de</th><th>Industria</th></tr></thead>
  <tbody>
    <tr><td class="name">Es simplemente el texto</td><td>Simplemente el</td><td>Relleno de las</td><td></td><td class="last">Quedando<span class="row-btn">Click here</span></td></tr>
    <tr><td class="name">Cuando un impresor</td><td>Pasajes de</td><td>Establecido hace</td><td></td><td class="last">Esencialmente igual<span class="row-btn">Click here</span></td></tr>
    <tr><td class="name">Es simplemente el texto</td><td>Simplemente el</td><td>Hace demasiado</td><td></td><td class="last">Quedando<span class="row-btn">Click here</span></td></tr>
    <tr><td class="name">Cuando un impresor</td><td>Que se puede</td><td>Relleno de las</td><td></td><td class="last">Quedando esen<span class="row-btn">Click here</span></td></tr>
    <tr><td class="name">De textos especimen</td><td>Pasajes de</td><td>Relleno de las</td><td></td><td class="last">Cialmente igual<span class="row-btn">Click here</span></td></tr>
    <tr><td class="name">Es simplemente el texto</td><td>Simplemente el</td><td>Hace demasiado</td><td></td><td class="last">Lmente igual<span class="row-btn">Click here</span></td></tr>
    <tr><td class="name">Cuando un impresor</td><td>Que se puede</td><td>Relleno de las</td><td>Establecido hace</td><td class="last">Quedando esencialmente igual<span class="row-btn">Click here</span></td></tr>
    <tr><td class="name">Es simplemente el texto</td><td>Pasajes de</td><td>Demasiado</td><td>Desconocido</td><td class="last">Esencialmente<span class="row-btn">Click here</span></td></tr>
    <tr><td class="name">Cuando un impresor</td><td>Simplemente el</td><td>Relleno de las</td><td>Hace demasiado</td><td class="last">Quedando<span class="row-btn">Click here</span></td></tr>
    <tr><td class="name">De textos especimen</td><td>Simplemente el</td><td>Establecido hace</td><td>Demasiado</td><td class="last">Cialmente igual<span class="row-btn">Click here</span></td></tr>
    <tr><td class="name">Cuando un impresor</td><td>Simplemente el</td><td>Demasiado</td><td>Establecido</td><td class="last">Quedando esencialmente<span class="row-btn">Click here</span></td></tr>
    <tr><td class="name">Es simplemente el texto</td><td>Simplemente el</td><td>Relleno de las</td><td>Desconocido</td><td class="last">Quedando esencialmente igual<span class="row-btn">Click here</span></td></tr>
  </tbody>
</table>

<ul class="dropdown admin-menu">
  <li>New</li>
  <li>Account</li>
  <li>Company Contact</li>
  <li>Note</li>
  <li>Message</li>
</ul>

<footer class="footer">
  <span class="copyright">Copyrights 2017. CareLedger. All rights reserved.</span>
  <span class="contact-btn">Contact us</span>
</footer>
</body>
</html>
```